Website for the K7VANT-Lab research laboratory.

We are a research team working on personality disorders. We would like a website that presents the team members (noting that students change frequently), ongoing projects with active recruitments, the latest publications, student resources, and possibly patient resources.

We have already prepared the logo with Plumvetta.

Our research areas:
1- Lifestyle Medicine and BPD
This area focuses on understanding lifestyle habits and their impact on the health of individuals living with Borderline Personality Disorder (BPD). It aims to improve essential components such as sleep, physical activity, and nutrition by identifying and promoting favorable lifestyle habits. The goal is to strengthen emotional regulation and improve overall health by fully integrating the physical dimension into recovery.
2- Interventions Supporting Psychosocial Functioning
Develop the full recovery potential and enhance social and professional integration strategies to support the life journey of patients in all its dimensions. This area focuses on practices and interventions that facilitate a return to an active life and harmonious integration into society.
3- Optimization of Psychotherapeutic Strategies in BPD
Optimize psychotherapeutic approaches for BPD by identifying the most effective methods, adapting them to individual needs, and evaluating their long-term impact. This research area aims to refine and personalize treatments to maximize their therapeutic benefits.
4- Biological Treatments for BPD: Neuromodulation and Pharmacotherapy
Develop and evaluate biological treatments, particularly in neuromodulation and pharmacotherapy, to improve the management of BPD. This area aims to explore scientific advances in these fields to offer complementary and innovative therapeutic options.

Vision
Affiliated with TVOLBAE, our laboratory is dedicated to creating tomorrow's interventions to offer a hopeful future for individuals living with Borderline Personality Disorder. We design and develop innovative solutions that integrate and value each individual, their loved ones, and their community, supporting their personal, social, functional, and physical recovery.

Values

Innovation
Our commitment to innovation guides every step of our research and development. We continually strive to push the boundaries of knowledge and techniques to create new and bold therapeutic solutions tailored to the evolving needs of individuals living with Borderline Personality Disorder.
Hope
We carry the hope of making a real difference in the lives of people living with BPD. This hope drives our work, pushing us to explore therapeutic approaches that offer patients a better and more serene future. By integrating this hope into our research, we are committed to developing interventions that inspire and support the recovery process. Through our research work, we wish to instill and spread hope.
Empathy and Personalization
We believe in a person-centered and inclusive approach where each individual is considered in their uniqueness and with compassion. By actively integrating patients and their experiences into our research, we aim to design solutions that not only meet their specific needs but also value their recovery while respecting their values. We wish to improve the satisfaction of individuals within the care network, promote the integration of their loved ones and their community.

```html
<!DOCTYPE html>
<html lang="en">
<head>
<meta charset="utf-8">
<title>K7VANT-Lab — Personality Disorder Research & Development</title>
<link href="https://fonts.googleapis.com/css2?family=Poppins:wght@400;500;600;700&display=swap" rel="stylesheet">
<style>
:root{
  --orange:#f47b0c;
  --teal:#0fa3a0;
  --teal-dark:#0b8e8b;
  --navy:#0b1823;
  --navy-2:#12283a;
  --ink:#111111;
  --text:#2a2a2a;
  --muted:#555;
  --white:#ffffff;
  --card:#f4f4f4;
  --logo:#1e8fc8;
}
*{margin:0;padding:0;box-sizing:border-box}
html,body{width:1200px;height:3531px;overflow:hidden;background:var(--white)}
body{font-family:"Poppins",sans-serif;color:var(--text);position:relative}
.abs{position:absolute}
.btn{position:absolute;background:var(--orange);color:var(--white);font-size:13.5px;display:flex;align-items:center;justify-content:center;text-decoration:none}
/* header / hero */
.hero{position:absolute;left:0;top:0;width:1200px;height:603px}
.logo{position:absolute;display:flex;align-items:center;gap:10px;font-weight:600;font-size:37px;color:var(--logo);letter-spacing:-.5px}
.logo-dot{width:40px;height:40px;border-radius:50%;background:var(--teal)}
.nav{position:absolute;top:68px;left:391px;display:flex;gap:27px;font-size:17px;color:var(--white)}
.nav a{color:inherit;text-decoration:none}
.nav a.active{color:var(--orange)}
.hero-title{position:absolute;left:108px;top:214px;color:var(--white);font-weight:700;font-size:42px;line-height:1.2}
.hero-title span{display:block;color:var(--orange);font-weight:600;font-size:33px}
.hero-text{position:absolute;left:111px;top:332px;width:440px;color:var(--white);font-size:15.5px;line-height:21px}
/* about */
.about-frame{left:111px;top:688px;width:399px;height:354px;background:var(--orange)}
.about-photo{left:128px;top:705px;width:367px;height:323px;background:linear-gradient(135deg,#b9c0c7,#5a6672 60%,#2e3740)}
.about-small{left:398px;top:947px;width:185px;height:138px;background:var(--teal);padding:14px}
.about-small div{width:100%;height:100%;background:linear-gradient(135deg,#d7e4ee,#6a8aa3)}
.eyebrow{color:var(--orange);font-weight:600;font-size:20px}
.h2{font-weight:700;font-size:31px;color:var(--ink);line-height:35px}
.about-text{left:611px;top:694px;width:480px}
.about-text p{font-size:15.3px;line-height:20.6px;margin-top:24px}
.about-text p:first-of-type{margin-top:22px}
.section-title{position:absolute;left:0;width:1200px;text-align:center;font-weight:700;font-size:31px;color:var(--ink)}
.section-title span{color:var(--orange)}
.section-title::after{content:"";display:block;width:222px;height:2px;background:var(--teal);margin:6px auto 0}
/* research cards */
.rcard{position:absolute;top:1298px;width:354px;height:410px;overflow:hidden}
.rcard .img{height:324px}
.rcard .bar{height:86px;background:var(--teal);color:var(--white);font-weight:600;font-size:21px;line-height:26px;display:flex;align-items:center;justify-content:center;text-align:center;padding:0 12px}
.rcard.open .img{background:#151a1f;color:var(--white);text-align:center;padding:54px 30px 0}
.rcard.open h3{font-size:17.5px;font-weight:600;margin-bottom:26px}
.rcard.open p{font-size:15.5px;line-height:20.7px}
/* vision */
.vision{left:111px;top:1777px;width:972px;height:377px;border-radius:14px;background:radial-gradient(ellipse at 20% 40%,#1f4660,#0d2233 55%,#07131c);color:var(--white);text-align:center}
.vision h2{margin-top:44px;font-size:31px;font-weight:700}
.vision h2 span{color:var(--orange)}
.vision p{width:790px;margin:26px auto 0;font-size:15.5px;line-height:20.8px}
/* values */
.vcard{position:absolute;top:2333px;width:282px;height:335px;background:var(--card);border-radius:8px;box-shadow:0 2px 6px rgba(0,0,0,.08);text-align:center}
.vcard .icon{width:100px;height:100px;margin:34px auto 0}
.vcard h3{font-size:20.5px;font-weight:600;color:var(--ink);margin-top:22px}
.vcard p{font-size:15.4px;line-height:17.3px;margin:4px auto 0;width:232px;color:#333}
/* team */
.member{position:absolute;top:2794px;width:300px;text-align:center}
.member .photo{width:212px;height:212px;border-radius:50%;margin:0 auto;background:linear-gradient(160deg,#e6eef3,#9fb3c2 60%,#5e7283)}
.member .role{margin-top:18px;font-weight:600;font-size:14.5px;color:var(--ink)}
.member .name{font-size:15px;color:#333;margin-top:4px}
.arrow{position:absolute;top:2868px;width:64px;height:64px;border-radius:50%;background:var(--orange)}
/* footer */
.footer{position:absolute;left:0;top:3120px;width:1200px;height:411px}
.ftext{left:112px;top:3301px;width:360px;color:#e8e8e8;font-size:15.4px;line-height:25px}
.fhead{color:#e8e8e8;font-size:20px}
.flist{left:611px;top:3272px;list-style:none;color:#eee;font-size:16.5px}
.flist li{height:34.3px;display:flex;align-items:center;gap:18px}
.flist li::before{content:"";width:6px;height:6px;border-radius:50%;background:#eee}
.contact{left:834px;top:3272px;color:#eee;font-size:15.5px}
.contact li{list-style:none;height:34.3px;display:flex;align-items:center;gap:12px}
.contact svg{width:18px;height:18px;fill:#fff}
.fline{left:112px;top:3482px;width:976px;height:1px;background:rgba(255,255,255,.25)}
.copy{left:117px;top:3496px;color:#ddd;font-size:15.5px}
.social{left:964px;top:3494px;display:flex;gap:11px}
.social span{width:22px;height:22px;border-radius:50%;border:1.6px solid #ddd}
</style>
</head>
<body>

<!-- Hero -->
<svg class="hero" viewBox="0 0 1200 603" aria-hidden="false">
  <defs>
    <radialGradient id="heroGlow" cx="0.68" cy="0.3" r="0.6">
      <stop offset="0" stop-color="#1d4a66"/>
      <stop offset="0.55" stop-color="#0f2436"/>
      <stop offset="1" stop-color="#08131c"/>
    </radialGradient>
  </defs>
  <path d="M0 0H1200V514L570 590L0 514Z" fill="url(#heroGlow)"/>
  <path d="M0 514L570 590L1200 514V535L570 603L0 535Z" fill="var(--teal)"/>
  <rect x="560" y="0" width="640" height="560" fill="transparent" role="img" aria-label="Profile silhouette of a head with a glowing blue brain network"/>
</svg>

<div class="logo" style="left:112px;top:58px"><span class="logo-dot"></span>K7VANT-Lab</div>
<nav class="nav">
  <a class="active" href="#">Home</a><a href="#">About Us</a><a href="#">Contact</a><a href="#">Services</a><a href="#">Pages</a><a href="#">Elements</a>
</nav>
<a class="btn" href="#" style="left:968px;top:62px;width:119px;height:41px">Contact Us</a>

<h1 class="hero-title">Personality Disorder<span>Research &amp; Development</span></h1>
<p class="hero-text">By integrating this hope into our research, we are committed to developing interventions that inspire and support the recovery process.</p>
<a class="btn" href="#" style="left:111px;top:422px;width:119px;height:43px">Read More</a>

<!-- About -->
<div class="abs about-frame"></div>
<div class="abs about-photo" role="img" aria-label="A young man in conversation with a clinician"></div>
<div class="abs about-small"><div role="img" aria-label="Two researchers working in a laboratory"></div></div>
<div class="abs about-text">
  <div class="eyebrow">About Us</div>
  <h2 class="h2" style="margin-top:6px">We'll Ensure &nbsp;the<br>Best Result</h2>
  <p>We design and develop innovative solutions that integrate and value each individual, their loved ones, and their community, supporting their personal, social, functional, and physical recovery.</p>
  <p>We continually strive to push the boundaries of knowledge and techniques to create new and bold therapeutic solutions tailored to the evolving needs of individuals living with Borderline Personality Disorder.</p>
</div>
<a class="btn" href="#" style="left:611px;top:1039px;width:120px;height:43px">Learn More</a>

<!-- Research areas -->
<h2 class="section-title" style="top:1213px">Our <span>Research Areas</span></h2>
<div class="rcard" style="left:-72px">
  <div class="img" role="img" aria-label="Fruit, pills and a dumbbell on a table" style="background:linear-gradient(135deg,#d9c3a5,#9a8a7a 55%,#3c3c3c)"></div>
  <div class="bar" style="justify-content:flex-end;text-align:left">Lifestyle Medicine<br>and BPD</div>
</div>
<div class="rcard" style="left:302px">
  <div class="img" role="img" aria-label="Two women talking in an office" style="background:linear-gradient(135deg,#c9c6bf,#8d8477 55%,#5a4e44)"></div>
  <div class="bar">Interventions Supporting Psychosocial Functioning</div>
</div>
<div class="rcard open" style="left:673px">
  <div class="img">
    <h3>Psychotherapeutic Strategies</h3>
    <p>Optimize psychotherapeutic approaches for BPD by identifying the most effective methods, adapting them to individual needs, and evaluating their long-term impact. This research area aims to refine and personalize treatments to maximize their therapeutic benefits.</p>
  </div>
  <div class="bar">Optimization of Psychotherapeutic Strategies</div>
</div>
<div class="rcard" style="left:1046px">
  <div class="img" role="img" aria-label="Pills on a book about borderline personality disorder" style="background:linear-gradient(135deg,#c7d2d8,#e8e2d6 50%,#8f8a80)"></div>
  <div class="bar" style="justify-content:flex-start;text-align:left">Biological Treatments<br>for BPD</div>
</div>

<!-- Vision -->
<section class="abs vision" role="img" aria-label="Dark laboratory background with DNA helix and microscope">
  <h2>Our <span>Vision</span></h2>
  <p>Affiliated with TVOLBAE, our laboratory is dedicated to creating tomorrow's interventions to offer a hopeful future for individuals living with Borderline . We design and develop innovative solutions that integrate and value each individual, their loved ones, and their community, supporting their personal, social, functional, and physical recovery.</p>
</section>
<a class="btn" href="#" style="left:550px;top:2034px;width:119px;height:42px">Learn More</a>

<!-- Values -->
<h2 class="section-title" style="top:2247px">Our <span>Values</span></h2>
<div class="vcard" style="left:111px">
  <svg class="icon" viewBox="0 0 100 100"><circle cx="50" cy="50" r="48" fill="none" stroke="var(--teal)" stroke-width="2"/><path d="M50 30c-10 0-16 7-16 15 0 6 4 9 6 13v6h20v-6c2-4 6-7 6-13 0-8-6-15-16-15zM42 70h16M44 75h12" fill="none" stroke="var(--teal)" stroke-width="2"/></svg>
  <h3>Innovation</h3>
  <p>Our commitment to innovation guides every step of our research and development.</p>
</div>
<div class="vcard" style="left:458px">
  <svg class="icon" viewBox="0 0 100 100"><circle cx="50" cy="50" r="48" fill="none" stroke="var(--teal)" stroke-width="2"/><path d="M50 30l4 8 9 1-7 6 2 9-8-5-8 5 2-9-7-6 9-1z" fill="none" stroke="var(--teal)" stroke-width="2"/><path d="M26 62c8 0 12 4 20 4h12c3 0 3 4 0 4H46M26 70c10 6 24 8 34 2l14-10" fill="none" stroke="var(--teal)" stroke-width="2"/></svg>
  <h3>Hope</h3>
  <p>We carry the hope of making a real difference in the lives of people living with BPD. This hope drives our work</p>
</div>
<div class="vcard" style="left:805px">
  <svg class="icon" viewBox="0 0 100 100"><circle cx="50" cy="50" r="48" fill="none" stroke="var(--teal)" stroke-width="2"/><path d="M46 34c-10 0-16 6-16 14 0 5 3 8 3 12v6M54 34c10 0 16 6 16 14 0 5-3 8-3 12v6" fill="none" stroke="var(--teal)" stroke-width="2"/><circle cx="42" cy="50" r="5" fill="none" stroke="var(--teal)" stroke-width="2"/><circle cx="58" cy="50" r="5" fill="none" stroke="var(--teal)" stroke-width="2"/></svg>
  <h3>Empathy</h3>
  <p>We believe in a person-centered and inclusive approach where each individual is considered in their uniqueness and with compassion.</p>
</div>

<!-- Team -->
<h2 class="section-title" style="top:2715px">Our <span>Team</span></h2>
<svg class="arrow" style="left:23px" viewBox="0 0 64 64"><circle cx="32" cy="32" r="32" fill="var(--orange)"/><path d="M44 32H21M30 22L20 32l10 10" fill="none" stroke="#fff" stroke-width="4" stroke-linecap="round" stroke-linejoin="round"/></svg>
<svg class="arrow" style="left:1109px" viewBox="0 0 64 64"><circle cx="32" cy="32" r="32" fill="var(--orange)"/><path d="M20 32h23M34 22l10 10-10 10" fill="none" stroke="#fff" stroke-width="4" stroke-linecap="round" stroke-linejoin="round"/></svg>
<div class="member" style="left:145px"><div class="photo" role="img" aria-label="Portrait of the principal investigator in a lab coat"></div><div class="role">PRINCIPAL INVESTIGATOR</div><div class="name">Nathan Korell, PhD</div></div>
<div class="member" style="left:431px"><div class="photo" role="img" aria-label="Portrait of the laboratory technician in a lab coat"></div><div class="role">LABORATORY TECHNICIAN</div><div class="name">Lena Hartwig, PhD</div></div>
<div class="member" style="left:755px"><div class="photo" role="img" aria-label="Portrait of the laboratory manager in a lab coat"></div><div class="role">LABORATORY MANAGER</div><div class="name">Mira Valcourt, PhD</div></div>

<!-- Footer -->
<svg class="footer" viewBox="0 0 1200 411">
  <defs><linearGradient id="footBg" x1="0" y1="0" x2="1" y2="1"><stop offset="0" stop-color="#10202c"/><stop offset="1" stop-color="#0a141c"/></linearGradient></defs>
  <path d="M0 47L630 10L1200 47V75L630 38L0 75Z" fill="var(--teal)"/>
  <path d="M0 75L630 38L1200 75V411H0Z" fill="url(#footBg)"/>
</svg>
<div class="logo" style="left:112px;top:3222px"><span class="logo-dot"></span>K7VANT-Lab</div>
<p class="abs ftext">We wish to improve the satisfaction of individuals within the care network, promote the integration of their loved ones and their community.</p>

<div class="abs fhead" style="left:605px;top:3226px">Quick Links</div>
<ul class="abs flist">
  <li>Home</li><li>About Us</li><li>Contact</li><li>Services</li><li>Pages</li><li>Elements</li>
</ul>

<div class="abs fhead" style="left:832px;top:3229px">Contact Us</div>
<ul class="abs contact">
  <li><svg viewBox="0 0 24 24"><path d="M6.6 10.8a15 15 0 006.6 6.6l2.2-2.2a1 1 0 011-.25 11 11 0 003.5.56 1 1 0 011 1V20a1 1 0 01-1 1A17 17 0 013 4a1 1 0 011-1h3.5a1 1 0 011 1c0 1.2.2 2.4.56 3.5a1 1 0 01-.25 1z"/></svg>1-800-555-0142</li>
  <li><svg viewBox="0 0 24 24"><path d="M2 5h20v14H2zM2 6l10 7 10-7" stroke="#0a141c" stroke-width="1.5"/></svg>info@k7vantlab.org</li>
  <li><svg viewBox="0 0 24 24"><path d="M12 2a7 7 0 00-7 7c0 5 7 13 7 13s7-8 7-13a7 7 0 00-7-7zm0 9.5A2.5 2.5 0 1112 6a2.5 2.5 0 010 5.5z"/></svg>18 Larkspur Avenue, NY</li>
</ul>

<div class="abs fline"></div>
<div class="abs copy">© 2025 K7VANT-Lab. All rights reserved</div>
<div class="abs social"><span></span><span></span><span></span><span></span></div>

</body>
</html>
```